Post storm repair flyer

looking for an eye catching 6x9 postcard to send out to single family home owners advertising a "Post Storm Repair Special" explaining that after the recent hurricanes its very important to have your roof checked and any repairs fixed right away before they become a bigger more costly problem and that even though your home wasn't directly hit by the storm the high wind gust could've cause unseen damage.
offer $200 off any repair *some rules may apply
Lark Roofing
888.417.LARK
www.LarkRoofing.example

Roofing

```html
<!DOCTYPE html>
<html lang="en">
<head>
<meta charset="utf-8">
<title>Lark Roofing – Post Storm Repair Special Postcard</title>
<link href="https://fonts.googleapis.com/css2?family=Montserrat:wght@400;500;600;700;800&family=Rubik:wght@500;700;900&display=swap" rel="stylesheet">
<style>
  :root{
    --bg:#f2f2f0;
    --gold:#e8b33a;
    --gold-deep:#b8860b;
    --badge:#ffd21f;
    --charcoal:#3c3c3c;
    --ink:#1a1a1a;
    --offer:#e8141b;
    --paper:#ffffff;
    --panel:#e3e3e3;
    --rule:#b9b9b9;
  }
  *{box-sizing:border-box;margin:0;padding:0}
  html,body{width:1200px;height:1086px;overflow:hidden;background:var(--bg)}
  body{position:relative;font-family:"Montserrat",sans-serif;color:var(--ink)}

  .postcard{position:absolute;left:267px;width:665px;height:450px;overflow:hidden;background:var(--paper);box-shadow:0 6px 18px rgba(0,0,0,.18)}
  .postcard--front{top:74px}
  .postcard--back{top:573px;background:var(--panel)}

  /* front */
  .front-photo{position:absolute;inset:0;background:
    linear-gradient(180deg,rgba(255,255,255,.35) 0%,rgba(255,255,255,0) 45%),
    linear-gradient(160deg,#5a77a8 0%,#9aa3ad 22%,#d9dadb 45%,#b5b6b8 62%,#6f7174 100%)}
  .front-shapes{position:absolute;inset:0}
  .headline{position:absolute;left:0;right:0;text-align:center;font-weight:800;letter-spacing:-1px;line-height:1}
  .headline--top{top:32px;font-size:56px;color:var(--gold);text-shadow:0 2px 6px rgba(0,0,0,.25)}
  .headline--sub{top:91px;font-size:42px;color:#fff;text-shadow:0 2px 8px rgba(0,0,0,.45)}
  .headline--sub .light{font-weight:500}
  .front-intro{position:absolute;top:141px;left:0;right:0;text-align:center;font-size:13.5px;line-height:16px;color:#111}
  .phone{position:absolute;display:flex;align-items:center;gap:10px;font-weight:700;color:#fff}
  .phone svg{flex:none}
  .postcard--front .phone{left:23px;top:328px;font-size:23px}
  .brand{position:absolute;left:490px;top:330px;width:160px;text-align:center}
  .brand-name{display:flex;align-items:center;justify-content:center;gap:6px;font-size:17px;font-weight:700;color:var(--ink)}
  .brand-name .dot{width:12px;height:12px;background:var(--ink)}
  .brand-web{margin-top:26px;font-size:10.5px;font-weight:500;color:var(--ink)}

  /* badge */
  .offer-badge{position:absolute;text-align:center;font-family:"Rubik",sans-serif}
  .offer-badge svg{position:absolute;inset:0;width:100%;height:100%}
  .offer-text{position:absolute;left:0;right:0;line-height:1}
  .offer-get{font-weight:700;color:var(--ink)}
  .offer-amount{font-weight:900;color:var(--offer)}
  .offer-scope{font-weight:700;color:var(--ink)}
  .offer-note{font-family:"Montserrat",sans-serif;font-style:italic;color:#333;line-height:.9}
  .postcard--front .offer-badge{left:265px;top:266px;width:132px;height:152px}
  .postcard--front .offer-text{top:56px}
  .postcard--front .offer-get{font-size:16px}
  .postcard--front .offer-amount{font-size:26px;margin-top:2px}
  .postcard--front .offer-scope{font-size:15px;margin-top:2px}
  .postcard--front .offer-note{font-size:8px;margin-top:6px}

  /* back */
  .back-photo{position:absolute;inset:0;clip-path:polygon(0 0,540px 0,133px 215px,0 151px);background:
    linear-gradient(170deg,#3f6fb8 0%,#8ba6cc 30%,#c9ccd1 55%,#6d6e70 100%)}
  .address-side{position:absolute;inset:0;background:var(--paper);clip-path:polygon(545px 0,665px 0,665px 450px,333px 450px,333px 119px)}
  .stamp-box{position:absolute;left:558px;top:51px;width:74px;height:79px;border:1px solid #333}
  .address-line{position:absolute;left:362px;width:270px;height:1px;background:var(--rule)}
  .postcard--back .offer-badge{left:75px;top:93px;width:110px;height:126px}
  .postcard--back .offer-text{top:46px}
  .postcard--back .offer-get{font-size:13px}
  .postcard--back .offer-amount{font-size:21px;margin-top:1px}
  .postcard--back .offer-scope{font-size:12.5px;margin-top:1px}
  .postcard--back .offer-note{font-size:6.5px;margin-top:4px}
  .back-copy{position:absolute;left:24px;top:228px;width:300px}
  .back-heading{font-size:17.5px;font-weight:700;letter-spacing:-.3px;margin-bottom:6px}
  .back-copy p{font-size:12.8px;line-height:16px;margin-bottom:5px;color:#222}
  .call-bar{position:absolute;left:23px;top:388px;width:310px;height:47px;background:#000}
  .call-strip{position:absolute;left:23px;top:435px;width:310px;height:15px;background:var(--gold)}
  .postcard--back .phone{left:58px;top:397px;font-size:23px}
</style>
</head>
<body>

<section class="postcard postcard--front" aria-label="Postcard front">
  <div class="front-photo" role="img" aria-label="Photo of roofers working on the roof of a large white two-storey house"></div>
  <svg class="front-shapes" viewBox="0 0 665 450" aria-hidden="true">
    <polygon points="0,290 300,322 300,450 0,450" fill="var(--charcoal)"/>
    <polygon points="0,404 665,264 665,276 0,416" fill="var(--gold-deep)"/>
    <polygon points="0,416 665,276 665,450 0,450" fill="var(--gold)"/>
  </svg>
  <h1 class="headline headline--top">POST STORM</h1>
  <h2 class="headline headline--sub">REPAIR <span class="light">SPECIAL</span></h2>
  <p class="front-intro">After the recent hurricanes,<br>it’s crucial to have your roof<br>inspected and any necessary<br>repairs made promptly.</p>
  <div class="phone">
    <svg width="26" height="30" viewBox="0 0 26 30" aria-hidden="true"><polygon points="13,1 25,8 25,22 13,29 1,22 1,8" fill="none" stroke="var(--gold)" stroke-width="2"/><path d="M9 9c1-1 2-1 2.5 0l1 2c.3.7 0 1.2-.6 1.6 .6 1.6 1.6 2.8 3 3.6.5-.6 1-.8 1.7-.4l1.9 1.2c.8.5.6 1.5-.2 2.3-1.3 1.3-4 .6-6.3-1.8S7.8 10.3 9 9z" fill="var(--gold)"/></svg>
    <span>888.417.LARK</span>
  </div>
  <div class="offer-badge">
    <svg viewBox="0 0 132 152" aria-hidden="true"><polygon points="66,3 129,39 129,113 66,149 3,113 3,39" fill="var(--badge)" stroke="var(--gold-deep)" stroke-width="3"/></svg>
    <div class="offer-text">
      <div class="offer-get">Get</div>
      <div class="offer-amount">$200 off</div>
      <div class="offer-scope">any repair</div>
      <div class="offer-note">*some rules<br>may apply</div>
    </div>
  </div>
  <div class="brand">
    <div class="brand-name"><span class="dot"></span>Lark Roofing</div>
    <div class="brand-web">LARKROOFING.EXAMPLE</div>
  </div>
</section>

<section class="postcard postcard--back" aria-label="Postcard back">
  <div class="back-photo" role="img" aria-label="Photo of roofers replacing shingles on a house under a blue sky"></div>
  <div class="address-side"></div>
  <div class="stamp-box"></div>
  <div class="address-line" style="top:209px"></div>
  <div class="address-line" style="top:241px"></div>
  <div class="address-line" style="top:273px"></div>
  <div class="address-line" style="top:304px"></div>
  <div class="address-line" style="top:335px"></div>
  <div class="offer-badge">
    <svg viewBox="0 0 132 152" aria-hidden="true"><polygon points="66,3 129,39 129,113 66,149 3,113 3,39" fill="var(--badge)" stroke="var(--gold-deep)" stroke-width="3"/></svg>
    <div class="offer-text">
      <div class="offer-get">Get</div>
      <div class="offer-amount">$200 off</div>
      <div class="offer-scope">any repair</div>
      <div class="offer-note">*some rules<br>may apply</div>
    </div>
  </div>
  <div class="back-copy">
    <h3 class="back-heading">Ensure Your Roof’s Safe Today</h3>
    <p>After the recent hurricanes, it’s crucial to have your roof inspected and any necessary repairs made promptly.</p>
    <p>Even if your home wasn’t directly hit by the storm, high wind gusts can cause unseen damage.</p>
  </div>
  <div class="call-bar"></div>
  <div class="call-strip"></div>
  <div class="phone">
    <svg width="22" height="24" viewBox="0 0 22 24" aria-hidden="true"><path d="M4 3c1.5-1.5 3-1.5 3.7 0l1.5 3c.4 1-.1 1.8-.9 2.4.9 2.4 2.4 4.2 4.5 5.4.7-.9 1.5-1.2 2.5-.6l2.8 1.8c1.2.7.9 2.2-.3 3.4-2 2-6 .9-9.5-2.7S2.2 4.8 4 3z" fill="var(--gold)"/></svg>
    <span>888.417.LARK</span>
  </div>
</section>

</body>
</html>
```